Verpackungen für Temperatur-Kalibrierprodukte
Zielgruppe
Wir sind eine Firma, die Temperatur-Kalibrierprodukte vertreibt und suchen ein hochwertiges Design für die Verpackung unserer High-End Thermometer. Unsere Zielgruppe sind Firmen aus Industrie, Forschung und Entwicklung.
Aufgabenstellung
Wir suchen ein Design für eine Magnetbox, in der unsere hochwertigen Thermometer transportiert und aufbewahrt werden. Das Design soll sich an unsere Website-Gestaltung anlehnen, bzw. dazu passen.
Auf die Verpackung sollte das Logo, sowie das Wort 'Präzisionsthermometer'.
Innenmaße der Verpackung:
60 x 13 x 4,5 / 4,5 cm (Breite x Tiefe x Höhe/Klappenhöhe)
Material: 1,8 mm Graubpappe innen weiß
Bezugsmaterial: außen weißes Kraftpapier 157g
Bei Bedarf können wir weiteres Bildmaterial zur Verfügung stellen (siehe Website).

```html
<!DOCTYPE html>
<html lang="de">
<head>
<meta charset="utf-8">
<title>Termora Präzisionsmesser – Verpackungsbezug</title>
<link rel="stylesheet" href="https://fonts.googleapis.com/css2?family=Big+Shoulders+Display:wght@700;800&family=Montserrat:wght@400;600;700&display=swap">
<style>
  :root {
    --stage: #8a8a8a;
    --metal-dark: #b9bcc0;
    --metal-mid: #d3d5d8;
    --metal-light: #eef0f2;
    --signal-red: #c3261e;
    --signal-red-dark: #8e1812;
    --ink: #1d1d1d;
    --ink-soft: #333333;
  }
  html, body {
    margin: 0;
    padding: 0;
    width: 1200px;
    height: 1200px;
    overflow: hidden;
    background: var(--stage);
  }
  .sheet {
    position: absolute;
    left: 0;
    top: 257px;
    width: 1200px;
    height: 686px;
    display: block;
  }
  .title-display {
    font-family: "Big Shoulders Display", "Arial Narrow", sans-serif;
    font-weight: 800;
  }
  .brand-name {
    font-family: "Montserrat", Arial, sans-serif;
    font-weight: 600;
    fill: var(--ink);
  }
  .maker-name {
    font-family: "Montserrat", Arial, sans-serif;
    font-weight: 700;
    fill: var(--ink);
  }
  .maker-tagline {
    font-family: "Montserrat", Arial, sans-serif;
    font-weight: 400;
    fill: var(--ink-soft);
  }
</style>
</head>
<body>
<svg class="sheet" viewBox="0 0 1177 673" xmlns="http://www.w3.org/2000/svg" aria-label="Bezugsbogen der Magnetbox, flach ausgelegt">
  <defs>
    <linearGradient id="brushed-metal" x1="0" y1="0" x2="1" y2="0">
      <stop offset="0" stop-color="var(--metal-dark)"/>
      <stop offset="0.35" stop-color="var(--metal-mid)"/>
      <stop offset="0.6" stop-color="var(--metal-light)"/>
      <stop offset="0.66" stop-color="#f7f8f9"/>
      <stop offset="0.8" stop-color="var(--metal-mid)"/>
      <stop offset="1" stop-color="var(--metal-dark)"/>
    </linearGradient>
    <linearGradient id="metal-shade" x1="0" y1="0" x2="0" y2="1">
      <stop offset="0" stop-color="#ffffff" stop-opacity="0.15"/>
      <stop offset="0.5" stop-color="#000000" stop-opacity="0"/>
      <stop offset="1" stop-color="#000000" stop-opacity="0.06"/>
    </linearGradient>
    <linearGradient id="red-reflection" gradientUnits="userSpaceOnUse" x1="0" y1="552" x2="0" y2="596">
      <stop offset="0" stop-color="var(--signal-red)" stop-opacity="0.45"/>
      <stop offset="1" stop-color="var(--signal-red)" stop-opacity="0"/>
    </linearGradient>
    <linearGradient id="ink-reflection" gradientUnits="userSpaceOnUse" x1="0" y1="305" x2="0" y2="352">
      <stop offset="0" stop-color="var(--ink)" stop-opacity="0.3"/>
      <stop offset="1" stop-color="var(--ink)" stop-opacity="0"/>
    </linearGradient>
  </defs>

  <!-- Surface -->
  <rect class="surface" x="0" y="0" width="1177" height="673" fill="url(#brushed-metal)"/>
  <rect class="surface-shade" x="0" y="0" width="1177" height="673" fill="url(#metal-shade)"/>

  <!-- Lid panel, reading upside down -->
  <g class="lid-title" transform="rotate(180 308.5 305)">
    <text class="title-display" x="83" y="305" textLength="454" lengthAdjust="spacingAndGlyphs" fill="var(--ink)">
      <tspan font-size="78">P</tspan><tspan font-size="60">RÄZISIONSMESSER</tspan>
    </text>
    <g transform="translate(0 610) scale(1 -1)">
      <text class="title-display" x="83" y="305" textLength="454" lengthAdjust="spacingAndGlyphs" fill="url(#ink-reflection)">
        <tspan font-size="78">P</tspan><tspan font-size="60">RÄZISIONSMESSER</tspan>
      </text>
    </g>
  </g>

  <g class="maker-block maker-block--lid" transform="rotate(180 865 334.5)">
    <rect x="770" y="312" width="45" height="45" fill="var(--signal-red)"/>
    <text class="maker-name" x="858" y="332" font-size="13">Vornhalt</text>
    <text class="maker-tagline" x="858" y="350" font-size="10.5">Präzision in Temperatur</text>
  </g>

  <!-- Left side flap -->
  <g class="brand-mark brand-mark--side-left" transform="rotate(90 40 480)">
    <circle cx="-30" cy="480" r="11" fill="var(--ink-soft)"/>
    <text class="brand-name" x="-12" y="489" font-size="26">Termora</text>
  </g>

  <!-- Front face -->
  <g class="brand-mark brand-mark--front">
    <circle cx="157" cy="512" r="29" fill="var(--ink-soft)"/>
    <text class="brand-name" x="202" y="533" font-size="58">Termora</text>
  </g>

  <g class="product-title">
    <text class="title-display" x="548" y="552" textLength="467" lengthAdjust="spacingAndGlyphs" fill="var(--signal-red)" stroke="var(--signal-red-dark)" stroke-width="1.2">
      <tspan font-size="190">P</tspan><tspan font-size="132">RÄZISIONSMESSER</tspan>
    </text>
    <g transform="translate(0 1104) scale(1 -1)">
      <text class="title-display" x="548" y="552" textLength="467" lengthAdjust="spacingAndGlyphs" fill="url(#red-reflection)">
        <tspan font-size="190">P</tspan><tspan font-size="132">RÄZISIONSMESSER</tspan>
      </text>
    </g>
  </g>

  <text class="title-display product-subtitle" x="553" y="663" textLength="459" lengthAdjust="spacingAndGlyphs" fill="var(--ink)">
    <tspan font-size="74">P</tspan><tspan font-size="49">RÄZISIONSMESSER</tspan>
  </text>

  <g class="maker-block maker-block--front">
    <rect x="130" y="609" width="45" height="45" fill="var(--signal-red)"/>
    <text class="maker-name" x="219" y="636" font-size="13">Vornhalt</text>
    <text class="maker-tagline" x="219" y="654" font-size="10.5">Präzision in Temperatur</text>
  </g>

  <!-- Right side flap -->
  <g class="brand-mark brand-mark--side-right" transform="rotate(-90 1140 495)">
    <circle cx="1082" cy="495" r="9" fill="var(--ink-soft)"/>
    <text class="brand-name" x="1097" y="503" font-size="23">Termora</text>
  </g>
</svg>
</body>
</html>
```